Christmas Party Poster

I am promoting a Christmas Party for teenagers age 13-17 years old. The event is the first of its kind in our area, Weston Super Mare. The ticket price is to include food, soft drink's, music, entertainment.

There is nothing else of its kind in the the area or surrounding towns so a one of a kind event and new to the town. I would like the poster to be as simple and less busy as possible while still clearly showing the key information, anything that can be added it to show its a Christmas party for teenagers would be great. Also this is aimed at 13-17 year old's so as current and modern a design as possible.
Updates

A big thank you for the designs so far, As this is my first project I'm just getting the hang of what to ask for. I have slightly updated the brief and I now realize less is more, so long as the poster has the key elements of event name, date, time's, location, price and age range. The rest I should have been more flexible on. Thank you for your patience.

Target Market(s)

My Target Market are teenagers specifically 13-17 year olds

Industry/Entity Type

Town

Requirements
Must have
• The Title 'Frostgleam' The venue is 'The Amber Pavilion h-b-t', Phone Number '01852 630284' Date '19th December'. Times '19.00 - 23.00'. Strictly u18 or age 13-17 years. Ticket price of £20. Face book 'frost gleam hbt' limited 4 tickets per person
Nice to have
• Christmas Party, Photo of your night out. Food and drink included
Should not have
• no worded reference to Santa, snowmen, reindeer, disco, try to keep out as not to offend cool teenagers.

```html
<!DOCTYPE html>
<html lang="en">
<head>
<meta charset="utf-8">
<title>Frostgleam Christmas Party Poster</title>
<link href="https://fonts.googleapis.com/css2?family=Bowlby+One&family=Oswald:wght@500;700&display=swap" rel="stylesheet">
<style>
  :root {
    --stage: #f4f4f4;
    --pink: #e3176e;
    --pink-deep: #b80d55;
    --pink-light: #f25a9b;
    --blue: #1fa9e1;
    --blue-deep: #0c6fa6;
    --white: #ffffff;
    --black: #141414;
    --photo-warm: #a0522d;
    --photo-stage: #3b1a3f;
    --photo-party: #8a3a4a;
  }
  * { margin: 0; padding: 0; box-sizing: border-box; }
  html, body { width: 900px; height: 1200px; overflow: hidden; background: var(--stage); }
  .poster {
    position: absolute; left: 50px; top: 0; width: 800px; height: 1200px; overflow: hidden;
    background: radial-gradient(ellipse at 50% 40%, var(--pink-light) 0%, var(--pink) 45%, var(--pink-deep) 100%);
    font-family: "Oswald", sans-serif; color: var(--white);
  }
  .bokeh { position: absolute; inset: 0; }
  .title {
    position: absolute; left: 0; right: 0; top: 30px; text-align: center;
    font-family: "Bowlby One", sans-serif; font-size: 150px; line-height: 0.88; letter-spacing: 2px;
    color: var(--white); -webkit-text-stroke: 4px var(--blue);
    text-shadow: 6px 6px 0 var(--blue-deep);
  }
  .subtitle {
    position: absolute; left: 0; right: 0; top: 300px; text-align: center;
    font-family: "Bowlby One", sans-serif; font-size: 50px; color: var(--white);
    text-shadow: 3px 3px 0 var(--blue-deep);
  }
  .age-band {
    position: absolute; left: 150px; top: 372px; width: 500px; height: 56px;
    background: var(--black); transform: rotate(-2deg);
    font-size: 36px; font-weight: 700; letter-spacing: 2px; text-align: center; line-height: 56px;
  }
  .limit-ribbon {
    position: absolute; left: 95px; top: 440px; width: 420px; height: 44px;
    background: var(--blue); transform: rotate(-8deg);
    font-size: 25px; font-weight: 500; text-align: center; line-height: 44px; z-index: 3;
  }
  .photo {
    position: absolute; border: 10px solid var(--white); box-shadow: 0 6px 14px rgba(0,0,0,.35);
  }
  .photo-fountain { left: 30px; top: 500px; width: 230px; height: 270px; transform: rotate(-5deg);
    background: linear-gradient(160deg, #d8a070, var(--photo-warm) 60%, #4a2412); }
  .photo-stage { left: 230px; top: 470px; width: 300px; height: 230px; transform: rotate(3deg);
    background: radial-gradient(circle at 50% 30%, #f07a3a, #b0306a 40%, var(--photo-stage) 80%); z-index: 2; }
  .photo-party { left: 505px; top: 430px; width: 270px; height: 210px; transform: rotate(-4deg);
    background: linear-gradient(135deg, #e0a080, var(--photo-party) 55%, #2a1020); }
  .price-badge {
    position: absolute; left: 590px; top: 640px; width: 180px; height: 170px; border-radius: 50%;
    background: var(--blue); z-index: 4; display: flex; align-items: center; justify-content: center;
    text-align: center; font-size: 34px; font-weight: 700; line-height: 1.05; text-transform: uppercase;
    box-shadow: 0 4px 10px rgba(0,0,0,.3);
  }
  .date-day {
    position: absolute; left: 0; right: 0; top: 690px; text-align: center;
    font-family: "Bowlby One", sans-serif; font-size: 120px; line-height: 1;
    -webkit-text-stroke: 3px var(--blue); text-shadow: 5px 5px 0 var(--blue-deep); z-index: 5;
  }
  .date-month {
    position: absolute; left: 0; right: 0; top: 810px; text-align: center;
    font-family: "Bowlby One", sans-serif; font-size: 128px; line-height: 1;
    -webkit-text-stroke: 3px var(--blue); text-shadow: 5px 5px 0 var(--blue-deep); z-index: 5;
  }
  .venue {
    position: absolute; left: 0; right: 0; top: 960px; text-align: center;
    font-size: 42px; font-weight: 500; text-transform: uppercase; letter-spacing: 1px;
  }
  .time-band {
    position: absolute; left: 210px; top: 1025px; width: 380px; height: 54px;
    background: var(--blue); transform: rotate(-2deg);
    font-size: 36px; font-weight: 700; text-align: center; line-height: 54px;
  }
  .social {
    position: absolute; left: 40px; top: 1120px; display: flex; align-items: center; gap: 14px;
    font-size: 34px; font-weight: 700; text-transform: uppercase;
  }
  .social-square { width: 44px; height: 44px; background: var(--white); }
  .box-office {
    position: absolute; left: 520px; top: 1100px; width: 260px; height: 80px;
    background: var(--blue); transform: rotate(-4deg);
    font-size: 20px; font-weight: 700; text-align: center; line-height: 1.2;
    display: flex; align-items: center; justify-content: center; text-transform: uppercase;
  }
</style>
</head>
<body>
<main class="poster">
  <svg class="bokeh" width="800" height="1200" aria-hidden="true">
    <g fill="#ffffff">
      <circle cx="70" cy="90" r="30" opacity=".12"/>
      <circle cx="720" cy="150" r="45" opacity=".1"/>
      <circle cx="640" cy="60" r="6" opacity=".8"/>
      <circle cx="110" cy="250" r="5" opacity=".8"/>
      <circle cx="700" cy="330" r="22" opacity=".15"/>
      <circle cx="40" cy="420" r="7" opacity=".7"/>
      <circle cx="760" cy="880" r="35" opacity=".12"/>
      <circle cx="60" cy="930" r="40" opacity=".1"/>
      <circle cx="120" cy="830" r="5" opacity=".8"/>
      <circle cx="690" cy="1010" r="6" opacity=".8"/>
      <circle cx="400" cy="1160" r="50" opacity=".08"/>
    </g>
  </svg>

  <h1 class="title">FROST<br>GLEAM</h1>
  <p class="subtitle">CHRISTMAS PARTY</p>
  <p class="age-band">AGE 13 - 17 YEARS ONLY</p>
  <p class="limit-ribbon">LIMITED 4 TICKETS PER PERSON</p>

  <div class="photo photo-fountain" role="img" aria-label="Photo of a chocolate fountain with party food"></div>
  <div class="photo photo-stage" role="img" aria-label="Photo of a crowd under coloured stage lights"></div>
  <div class="photo photo-party" role="img" aria-label="Photo of teenagers enjoying a night out"></div>

  <p class="price-badge">Ticket<br>price of<br>£20</p>

  <p class="date-day">19th</p>
  <p class="date-month">December</p>

  <p class="venue">@ The Amber Pavilion h-b-t</p>
  <p class="time-band">FROM 19.00 - 23.00</p>

  <div class="social"><span class="social-square"></span><span>Frost Gleam HBT</span></div>
  <p class="box-office">Advance tickets only,<br>box office (01852) 630284</p>
</main>
</body>
</html>
```